Business Card Design Project

Hello Designers, hope you are all aiming enjoy the weekend
I have the Business Logo (uploaded), you can alter the color which ever way you think would work,
Im looking for a simple yet striking feel, something which will stay memorable (I have uploaded 3 examples for you to flick through)
Information on the card, will just be the bare minimum,
Double Sided
Info being
i.e.
Name
Number
Website
ABN
Teo Marlowick
+482710365 (singapore)
+615093284 (Australia)
+790428153 (America)
www.lumoren-match.example
ABN 90817263
Enjoy,
Teo

```html
<!DOCTYPE html>
<html lang="en">
<head>
<meta charset="utf-8">
<title>Teo Marlowick – Business Card</title>
<link rel="stylesheet" href="https://fonts.googleapis.com/css2?family=Source+Sans+3:wght@400;600&display=swap">
<style>
  :root {
    --page-bg: #ffffff;
    --card-blue: #27a9e1;
    --accent-red: #d51f3c;
    --ink-dark: #1a1a1a;
    --ink-light: #ffffff;
  }
  * { margin: 0; padding: 0; box-sizing: border-box; }
  html, body {
    width: 1200px;
    height: 1126px;
    overflow: hidden;
    background: var(--page-bg);
  }
  body {
    position: relative;
    font-family: "Source Sans 3", "Myriad Pro", Arial, sans-serif;
  }
  .card {
    position: absolute;
    left: 226px;
    width: 723px;
    height: 413px;
    background: var(--card-blue);
    border-radius: 38px;
    box-shadow: 6px 8px 14px rgba(0, 0, 0, 0.35);
  }
  .card--front { top: 100px; }
  .card--back { top: 595px; }

  .brand {
    position: absolute;
    width: 220px;
    height: 220px;
    display: flex;
    flex-direction: column;
    align-items: center;
    justify-content: center;
    gap: 18px;
  }
  .card--front .brand { left: 42px; top: 34px; }
  .card--back .brand { left: 251px; top: 36px; }
  .brand__square {
    width: 96px;
    height: 96px;
    background: var(--accent-red);
  }
  .brand__name {
    font-size: 44px;
    font-weight: 600;
    color: var(--ink-light);
    line-height: 1;
  }

  .holder {
    position: absolute;
    left: 310px;
    top: 50px;
  }
  .holder__name {
    font-size: 50px;
    font-weight: 400;
    color: var(--accent-red);
    line-height: 1.1;
    margin-bottom: 22px;
  }
  .holder__details {
    list-style: none;
    font-size: 30px;
    line-height: 42px;
    color: var(--ink-dark);
  }

  .website {
    position: absolute;
    left: 0;
    width: 100%;
    text-align: center;
    font-size: 36px;
    color: var(--ink-light);
  }
  .card--front .website { top: 333px; }
  .card--back .website { top: 305px; }
</style>
</head>
<body>
  <section class="card card--front" aria-label="Card front">
    <div class="brand">
      <span class="brand__square"></span>
      <span class="brand__name">Lumoren</span>
    </div>
    <div class="holder">
      <h1 class="holder__name">Teo Marlowick</h1>
      <ul class="holder__details">
        <li>+482710365 (singapore)</li>
        <li>+615093284 (Australia)</li>
        <li>+790428153 (America)</li>
        <li>ABN 90817263</li>
      </ul>
    </div>
    <p class="website">www.lumoren-match.example</p>
  </section>

  <section class="card card--back" aria-label="Card back">
    <div class="brand">
      <span class="brand__square"></span>
      <span class="brand__name">Lumoren</span>
    </div>
    <p class="website">www.lumoren-match.example</p>
  </section>
</body>
</html>
```